Hi Tech startup needs a Business Card design

We need a business card design for a new company based in Russia called Velturo. We develop innovative telecom solutions for corporation and customers. Our initial product is an Qorvel app that directly connects customers to call centers and help desks via VoIP solutions without the need to dial (800) numbers saving time for customers and saving money for businesses.

We would like to see a design that communicates modern solutions and revolutionary approach. Not too cocky though.

Target Market(s)

the targeted audience is investors, partners, future directors and customers (large corporations)

Industry/Entity Type

Telecom

Requirements
Must have
• standard info

email / phone / plumtalk

```html
<!DOCTYPE html>
<html lang="en">
<head>
<meta charset="utf-8">
<title>Velturo – Business Card Designs</title>
<link rel="stylesheet" href="https://fonts.googleapis.com/css2?family=Open+Sans:wght@300;400;600&display=swap">
<style>
  :root {
    --ink: #222222;
    --bar-brown: #3a2414;
    --amber: #f8a91b;
    --sun: #f5c21f;
    --lemon: #f2ea2e;
    --paper: #ffffff;
    --backdrop-centre: #f4f4f4;
    --backdrop-edge: #9a9a9a;
  }
  * { margin: 0; padding: 0; box-sizing: border-box; }
  html, body { width: 1200px; height: 900px; overflow: hidden; }
  body {
    position: relative;
    font-family: "Open Sans", Arial, sans-serif;
    color: var(--ink);
    background: radial-gradient(ellipse 62% 60% at 50% 50%, var(--backdrop-centre) 0%, #d6d6d6 55%, var(--backdrop-edge) 100%);
  }
  .card {
    position: absolute;
    width: 515px;
    height: 290px;
    background: var(--paper);
    overflow: hidden;
    box-shadow: 2px 2px 3px rgba(0,0,0,0.55);
  }
  .card--front-a { left: 68px; top: 115px; }
  .card--back-white { left: 625px; top: 115px; }
  .card--front-b { left: 68px; top: 442px; }
  .card--back-yellow { left: 625px; top: 437px; background: linear-gradient(90deg, var(--amber) 0%, var(--sun) 55%, var(--lemon) 100%); }
  .card-art { position: absolute; left: 0; top: 0; width: 515px; height: 290px; }

  .brand { position: absolute; display: flex; align-items: center; }
  .brand-dot {
    width: 80px; height: 80px; border-radius: 50%;
    background: linear-gradient(135deg, var(--lemon), var(--amber));
    flex: none;
  }
  .brand-name {
    font-weight: 300;
    font-size: 50px;
    letter-spacing: -0.5px;
    color: var(--ink);
    line-height: 1;
  }
  .card--front-a .brand, .card--front-b .brand { left: 14px; top: 13px; gap: 14px; }
  .brand--stacked {
    flex-direction: column; gap: 16px;
    left: 0; right: 0;
  }
  .card--back-white .brand--stacked { top: 26px; }
  .card--back-yellow .brand--stacked { top: 83px; left: 130px; right: auto; width: 250px; }
  .brand--stacked .brand-dot { width: 90px; height: 90px; }
  .card--back-yellow .brand-dot { background: linear-gradient(135deg, var(--sun), var(--amber)); box-shadow: 0 0 0 4px rgba(255,255,255,0.35); }

  .holder-name { position: absolute; font-weight: 600; font-size: 20px; letter-spacing: 0.3px; text-transform: uppercase; line-height: 1; }
  .holder-role { position: absolute; font-size: 13px; line-height: 1; }
  .card--front-a .holder-name { left: 22px; top: 131px; }
  .card--front-a .holder-role { left: 22px; top: 158px; }
  .card--front-b .holder-name { left: 357px; top: 37px; font-weight: 400; }
  .card--front-b .holder-role { left: 356px; top: 62px; }
  .divider { position: absolute; left: 335px; top: 18px; width: 2px; height: 68px; background: var(--ink); }

  .contacts { position: absolute; list-style: none; font-size: 13px; letter-spacing: 0.2px; }
  .contacts li { display: flex; align-items: center; gap: 8px; height: 20.5px; }
  .contacts svg { width: 13px; height: 13px; flex: none; }
  .card--front-a .contacts { left: 22px; top: 192px; }
  .card--front-b .contacts { left: 108px; top: 125px; }
</style>
</head>
<body>

<!-- Front, layout A -->
<section class="card card--front-a">
  <svg class="card-art" viewBox="0 0 515 290" aria-hidden="true">
    <defs>
      <linearGradient id="bandA" x1="0" x2="1"><stop offset="0" stop-color="#f8a91b"/><stop offset="1" stop-color="#f2ea2e"/></linearGradient>
      <linearGradient id="discA" x1="0" y1="0" x2="1" y2="1"><stop offset="0" stop-color="#f2ea2e"/><stop offset="1" stop-color="#f8a91b"/></linearGradient>
    </defs>
    <rect x="0" y="181" width="400" height="2" fill="#f5b91c"/>
    <rect x="0" y="264" width="340" height="2.5" fill="#f5b91c"/>
    <rect x="0" y="271" width="515" height="19" fill="url(#bandA)"/>
    <circle cx="437" cy="215" r="112" fill="#ffffff"/>
    <circle cx="437" cy="215" r="113" fill="none" stroke="#f3e232" stroke-width="7"/>
    <circle cx="443" cy="218" r="100" fill="url(#discA)"/>
  </svg>
  <div class="brand"><span class="brand-dot"></span><span class="brand-name">velturo</span></div>
  <h2 class="holder-name">Anton Lerov</h2>
  <p class="holder-role">Director</p>
  <ul class="contacts">
    <li><svg viewBox="0 0 13 13"><rect x="0" y="0" width="13" height="13" rx="2" fill="#3a2414"/><rect x="3.5" y="2" width="6" height="9" rx="1" fill="#fff"/><rect x="4.5" y="3" width="4" height="6" fill="#3a2414"/></svg>0142 738 560</li>
    <li><svg viewBox="0 0 13 13"><rect x="0" y="1.5" width="13" height="10" rx="1.5" fill="#3a2414"/><path d="M1.5 3.5 L6.5 7.5 L11.5 3.5" fill="none" stroke="#fff" stroke-width="1.2"/></svg>antonlerov@velturo.com</li>
    <li><svg viewBox="0 0 13 13"><rect x="0" y="0" width="13" height="13" rx="2" fill="#3a2414"/></svg>@velturo</li>
  </ul>
</section>

<!-- Back, white -->
<section class="card card--back-white">
  <div class="brand brand--stacked"><span class="brand-dot"></span><span class="brand-name">velturo</span></div>
</section>

<!-- Front, layout B -->
<section class="card card--front-b">
  <svg class="card-art" viewBox="0 0 515 290" aria-hidden="true">
    <defs>
      <linearGradient id="swoopB" x1="0" x2="1"><stop offset="0" stop-color="#f2ea2e"/><stop offset="1" stop-color="#f8b81b"/></linearGradient>
      <linearGradient id="discB" x1="0" y1="0" x2="1" y2="1"><stop offset="0" stop-color="#f2ea2e"/><stop offset="1" stop-color="#f8a91b"/></linearGradient>
    </defs>
    <path d="M0 122 C 60 225, 210 272, 430 290 L0 290 Z" fill="url(#swoopB)"/>
    <path d="M0 188 C 90 245, 230 272, 360 276" fill="none" stroke="#ffffff" stroke-width="9"/>
    <circle cx="437" cy="213" r="112" fill="#ffffff"/>
    <circle cx="437" cy="213" r="113" fill="none" stroke="#f3e232" stroke-width="7"/>
    <circle cx="443" cy="216" r="100" fill="url(#discB)"/>
  </svg>
  <div class="brand"><span class="brand-dot"></span><span class="brand-name">velturo</span></div>
  <span class="divider"></span>
  <h2 class="holder-name">Anton Lerov</h2>
  <p class="holder-role">Director</p>
  <ul class="contacts">
    <li><svg viewBox="0 0 13 13"><rect x="0" y="0" width="13" height="13" rx="2" fill="#3a2414"/><rect x="3.5" y="2" width="6" height="9" rx="1" fill="#fff"/><rect x="4.5" y="3" width="4" height="6" fill="#3a2414"/></svg>0142 738 560</li>
    <li><svg viewBox="0 0 13 13"><rect x="0" y="1.5" width="13" height="10" rx="1.5" fill="#3a2414"/><path d="M1.5 3.5 L6.5 7.5 L11.5 3.5" fill="none" stroke="#fff" stroke-width="1.2"/></svg>antonlerov@velturo.com</li>
    <li><svg viewBox="0 0 13 13"><rect x="0" y="0" width="13" height="13" rx="2" fill="#3a2414"/></svg>@velturo</li>
  </ul>
</section>

<!-- Back, yellow -->
<section class="card card--back-yellow">
  <div class="brand brand--stacked"><span class="brand-dot"></span><span class="brand-name">velturo</span></div>
</section>

</body>
</html>
```